Second-Line Parade Announcement

Many members of our local chapter will be heading to New Orleans, LA, USA, in March 2019 to attend a large event hosted by our parent company. As part of this trip, we're hosting our own parade in The French Quarter (famous area of New Orleans), and we want to advertise this particular event, along with 1-2 others, on a one-page flyer.

This should be an invitation. What we're hosting is a "second-line parade," which is a much smaller, personal parade (not like big street parades), usually with 10-20 people.

Target Market(s)

Our own members

Colors

Designer to choose colors to be used in the design.

Requirements
Must have
• - Time & date (4:45 p.m., Sunday, March 17, 2019) and location (French Quarter)
• - Please include imagery of a New-Orleans-style parade (with traditional brass band) *OR* imagery of horn musicians (trumpeter, trombonist, etc.). It does not need to be a photo...could be an illustration...attached some for inspiration
• Final deliverable MUST include designer's raw files (e.g., .AI, .IDML, .PSD, etc.)
Nice to have
• I have included ads from our parent organization for the big conference, which can be used as part of your design or simply as inspiration for your design. I have also enclosed some sketch-like images of musicians that I don't own but that could be used as inspiration.
Should not have
• Please avoid imagery of alcohol, leprechauns (although a tasteful "leprechaun-style" hat would be okay), money/pots of gold and anything 'cartoon-like' or 'child-like.'
• Please leave some room ("white space") for additional details/instructions as they might arise.

```html
<!DOCTYPE html>
<html lang="en">
<head>
<meta charset="utf-8">
<title>Second-Line Parade</title>
<link rel="stylesheet" href="https://fonts.googleapis.com/css2?family=Alegreya:wght@400;500&family=Kaushan+Script&family=Fondamento&display=swap">
<style>
  :root {
    --backdrop: #e4e4e4;
    --kraft: #c9b99b;
    --violet: #6a2c92;
    --magenta: #c02a8e;
    --indigo: #3a3da3;
    --teal: #2a8fb0;
    --lime: #8fbf3a;
    --olive-green: #a9c23a;
    --sax-gold: #d9d24a;
    --paper-white: #ffffff;
    --badge-pink: #e3176f;
    --navy-ink: #2c3b8e;
    --tag-green: #2f9a55;
  }
  html, body {
    margin: 0;
    padding: 0;
    width: 1200px;
    height: 2275px;
    overflow: hidden;
    background: var(--backdrop);
  }
  .flyer {
    position: absolute;
    left: 110px;
    top: 482px;
    width: 980px;
    height: 1310px;
    background: var(--kraft);
    box-shadow: 0 6px 18px rgba(0,0,0,0.18);
  }
  .artwork {
    position: absolute;
    left: 20px;
    top: 20px;
    width: 940px;
    height: 1020px;
    overflow: hidden;
  }
  .artwork__backdrop {
    position: absolute;
    inset: 0;
    background:
      radial-gradient(ellipse 260px 420px at 40px 380px, rgba(42,143,176,0.6), rgba(42,143,176,0) 70%),
      radial-gradient(ellipse 260px 520px at 880px 300px, rgba(143,191,58,0.55), rgba(143,191,58,0) 70%),
      radial-gradient(ellipse 420px 360px at 420px 900px, rgba(58,61,163,0.6), rgba(58,61,163,0) 70%),
      linear-gradient(160deg, var(--violet) 0%, var(--magenta) 45%, var(--violet) 75%, var(--indigo) 100%);
  }
  .artwork__musician {
    position: absolute;
    left: 110px;
    top: 430px;
    width: 760px;
    height: 590px;
    border-radius: 46% 40% 0 0 / 40% 36% 0 0;
    background:
      radial-gradient(ellipse 220px 200px at 300px 120px, rgba(217,210,74,0.85), rgba(217,210,74,0) 75%),
      radial-gradient(ellipse 260px 320px at 560px 300px, rgba(47,154,85,0.85), rgba(47,154,85,0) 75%),
      linear-gradient(170deg, var(--olive-green) 0%, var(--lime) 50%, var(--teal) 100%);
    opacity: 0.9;
  }
  .chapter-mark {
    position: absolute;
    top: 38px;
    left: 0;
    width: 100%;
    display: flex;
    justify-content: center;
    align-items: center;
    gap: 16px;
  }
  .chapter-mark__dot {
    width: 54px;
    height: 54px;
    border-radius: 50%;
    background: var(--paper-white);
  }
  .chapter-mark__name {
    font-family: "Alegreya", Georgia, serif;
    font-weight: 400;
    font-size: 40px;
    color: var(--paper-white);
  }
  .title-rule {
    position: absolute;
    top: 136px;
    left: 200px;
    width: 540px;
    height: 2px;
    background: var(--paper-white);
  }
  .event-title {
    position: absolute;
    top: 150px;
    left: 0;
    width: 100%;
    margin: 0;
    text-align: center;
    color: var(--paper-white);
    font-weight: 400;
  }
  .event-title__kicker {
    display: block;
    font-family: "Alegreya", Georgia, serif;
    font-weight: 500;
    font-size: 76px;
    line-height: 1;
  }
  .event-title__main {
    display: block;
    font-family: "Kaushan Script", cursive;
    font-size: 130px;
    line-height: 1.05;
  }
  .date-badge {
    position: absolute;
    left: 60px;
    top: 700px;
    width: 250px;
    height: 250px;
    border-radius: 50%;
    border: 7px dotted var(--paper-white);
    box-sizing: border-box;
    display: flex;
    align-items: center;
    justify-content: center;
  }
  .date-badge__disc {
    width: 206px;
    height: 206px;
    border-radius: 50%;
    background: var(--badge-pink);
    color: var(--paper-white);
    font-family: "Alegreya", Georgia, serif;
    text-align: center;
    display: flex;
    flex-direction: column;
    justify-content: center;
    line-height: 0.95;
  }
  .date-badge__day { font-size: 76px; }
  .date-badge__month { font-size: 46px; }
  .date-badge__year { font-size: 46px; }
  .event-time {
    position: absolute;
    left: 70px;
    top: 1082px;
    width: 270px;
    margin: 0;
    font-family: "Fondamento", Georgia, serif;
    font-size: 54px;
    line-height: 1.1;
    color: var(--navy-ink);
    text-align: center;
  }
  .location-tag {
    position: absolute;
    left: 400px;
    top: 1072px;
    width: 560px;
    height: 120px;
    background: var(--tag-green);
    border-radius: 28px 6px 6px 28px;
    color: var(--paper-white);
  }
  .location-tag__hole {
    position: absolute;
    left: 26px;
    top: 48px;
    width: 24px;
    height: 24px;
    border-radius: 50%;
    background: var(--kraft);
  }
  .location-tag__label {
    position: absolute;
    left: 110px;
    top: 12px;
    font-family: "Fondamento", Georgia, serif;
    font-size: 36px;
  }
  .location-tag__place {
    position: absolute;
    left: 110px;
    top: 54px;
    font-family: "Fondamento", Georgia, serif;
    font-size: 50px;
    white-space: nowrap;
  }
</style>
</head>
<body>
  <article class="flyer">
    <div class="artwork">
      <div class="artwork__backdrop" role="img" aria-label="Flowing abstract shapes in purple, magenta, blue and green"></div>
      <div class="artwork__musician" role="img" aria-label="Illustration of a brass musician in a hat playing trumpet in front of a large saxophone, in green and yellow tones"></div>
      <div class="chapter-mark">
        <span class="chapter-mark__dot"></span>
        <span class="chapter-mark__name">Hudson Valley Chapter</span>
      </div>
      <div class="title-rule"></div>
      <h1 class="event-title">
        <span class="event-title__kicker">second~line</span>
        <span class="event-title__main">parade</span>
      </h1>
      <div class="date-badge">
        <div class="date-badge__disc">
          <span class="date-badge__day">17</span>
          <span class="date-badge__month">March</span>
          <span class="date-badge__year">2019</span>
        </div>
      </div>
    </div>
    <p class="event-time">Sunday<br>4:45 p.m</p>
    <div class="location-tag">
      <span class="location-tag__hole"></span>
      <span class="location-tag__label">location</span>
      <span class="location-tag__place">French Quarter</span>
    </div>
  </article>
</body>
</html>
```